Advertising flyer for proofreading business.

Hello everyone,

I need an advertising flyer for a new proofreading company in Australia.

I would like your design in be in two sizes:
- A4 (to be posted on noticeboards),
- A6 (to be printed in larger quantity to give away)
(please see the size specification file attached).

The text file is attached (Ad Text) and it contains lots of information. Please feel free to include your choice of text from the text file, but please include Poster title, and highlight 'ESL' and students discounts.

I understand that it is impossible to include the same amount of information on A6 and A4, so please feel free to chose what fits on each of them, but please keep the design similar.

I have attached our company logo, but feel free to adjust it to the poster design (feel free to change the color as well). The original logo file contains circle around it, please feel free to remove it and include only the typeset as it can be seen here: http://www.vellumcheck.com.au/.

Flyers will be printed, so please see the specification file for details.

I will do my best to respond to feedback as soon as possible.

I appreciate your participation, time and help,
Best wishes,
Radoslaw

Target Market(s)

Students, authors

Industry/Entity Type

Business

Colors

Designer to choose colors to be used in the design.

Requirements
Must have
• It would be good if poster is easy to spot on busy noticeboards and attract attention.
• Please keep the poster in the positive/optimistic mood, and so that it focuses on students, maybe photos of graduates(?).
• Poster title,
• Please include the list of proof-read documents as they are described in the attached text file (Ad Text).
• Please highlight students discounts and ESL.
Nice to have
• I would like to leave the creative freedom to all designers so at this point I have not adjusted the Look and Feel sliders. Please feel free to offer your own take on this.
• It would be nice if most of the text could be fit to the poster.

```html
<!DOCTYPE html>
<html lang="en">
<head>
<meta charset="utf-8">
<title>Vellumcheck – Proofreading Flyer</title>
<link rel="stylesheet" href="https://fonts.googleapis.com/css2?family=Open+Sans:wght@300;400;600;700&family=Cormorant+Garamond:wght@300&display=swap">
<style>
  :root {
    --teal: #1fa88e;
    --teal-dark: #178a74;
    --ink: #2f3132;
    --text: #3a3a3a;
    --paper: #f1f1f1;
    --white: #ffffff;
    --stage: #dcdcdc;
  }
  * { box-sizing: border-box; margin: 0; padding: 0; }
  html, body { width: 976px; height: 1200px; overflow: hidden; }
  body { background: var(--stage); font-family: "Open Sans", sans-serif; color: var(--text); }

  .flyer { position: absolute; left: 64px; top: 0; width: 848px; height: 1200px; background: var(--paper); overflow: hidden; }

  /* hero */
  .hero { position: absolute; left: 0; top: 0; width: 848px; height: 421px; }
  .hero-photo { position: absolute; inset: 0;
    background: linear-gradient(100deg, #7a5a4a 0%, #b28a70 35%, #c9a487 55%, #6d7f94 75%, #3b4f6e 100%); }
  .hero-shade { position: absolute; inset: 0; }
  .brand { position: absolute; left: 40px; top: 118px; display: flex; align-items: center; gap: 12px;
    font-weight: 300; font-size: 58px; color: var(--white); letter-spacing: -1px; }
  .brand-dot { width: 26px; height: 26px; border-radius: 50%; background: var(--teal); }
  .hero-rule { position: absolute; left: 20px; top: 228px; width: 290px; height: 2px; background: var(--teal); }
  .headline { position: absolute; left: 38px; top: 242px; font-weight: 600; font-size: 37px; line-height: 48px; color: var(--white); letter-spacing: -0.3px; }

  /* benefits band */
  .benefits { position: absolute; left: 0; top: 421px; width: 848px; height: 167px; background: var(--teal);
    box-shadow: 0 6px 10px rgba(0,0,0,0.18); }
  .benefit { position: absolute; top: 18px; display: flex; gap: 12px; color: var(--white); }
  .benefit-num { font-family: "Cormorant Garamond", serif; font-weight: 300; font-size: 54px; line-height: 44px; width: 24px; }
  .benefit-text { font-size: 17px; line-height: 21px; }
  .b1 { left: 38px; } .b1 .benefit-text { width: 170px; }
  .b2 { left: 288px; } .b2 .benefit-text { width: 210px; }
  .b3 { left: 556px; } .b3 .benefit-text { width: 250px; }

  /* section tags */
  .tag { position: absolute; left: 33px; height: 34px; width: 272px; background: var(--teal);
    clip-path: polygon(0 0, 94% 0, 100% 100%, 0 100%); color: var(--white);
    font-weight: 600; font-size: 21px; line-height: 34px; padding-left: 14px;
    filter: drop-shadow(0 3px 3px rgba(0,0,0,0.15)); }
  .tag-docs { top: 598px; }
  .tag-price { top: 903px; }

  .doc-list { position: absolute; left: 36px; top: 650px; list-style: none; font-size: 16px; line-height: 22.5px; color: var(--text); }
  .doc-list li { padding-left: 14px; position: relative; }
  .doc-list li::before { content: ""; position: absolute; left: 0; top: 8px; width: 7px; height: 7px; border-radius: 50%; border: 2px solid var(--teal); background: var(--white); }

  .price-list { position: absolute; left: 36px; top: 950px; list-style: none; font-size: 13px; line-height: 17px; color: var(--text); }
  .price-list li { position: relative; padding-left: 18px; margin-bottom: 7px; }
  .price-list li svg { position: absolute; left: 0; top: 2px; }
  .price-list .note { padding-left: 18px; }

  /* testimonial */
  .hand-phone { position: absolute; left: 440px; top: 612px; width: 408px; height: 490px;
    background: radial-gradient(ellipse at 40% 45%, #2a2a2a 0%, #3a3a3a 32%, #e6c2a4 48%, #f0dccb 70%, rgba(241,241,241,0) 90%); }
  .quote-card { position: absolute; left: 515px; top: 725px; width: 190px; height: 300px; background: var(--white);
    transform: rotate(-22deg); transform-origin: center; padding: 36px 14px 0 16px; font-size: 13px; line-height: 16px; color: #333; font-style: italic; }
  .quote-card .mark { color: var(--teal); font-weight: 700; font-style: normal; font-size: 20px; }
  .quote-card .who { margin-top: 26px; font-style: normal; font-size: 12px; line-height: 15px; }
  .quote-card .mini-brand { margin-top: 18px; font-style: normal; font-weight: 300; font-size: 22px; color: #333; text-align: center; }

  /* footer */
  .footer { position: absolute; left: 0; top: 1102px; width: 848px; height: 98px; background: var(--ink); }
  .footer-call { position: absolute; left: 42px; top: 32px; font-size: 23px; color: var(--teal); font-weight: 400; }
  .contact { position: absolute; left: 562px; top: 1086px; width: 286px; height: 114px; background: var(--teal);
    clip-path: polygon(12px 0, 100% 0, 100% 100%, 0 100%, 0 28px); padding: 14px 0 0 24px; color: var(--white); }
  .contact-row { display: flex; align-items: center; gap: 12px; font-weight: 600; font-size: 18px; line-height: 29px; }
  .contact-row.small { font-size: 17px; }
</style>
</head>
<body>
<main class="flyer">

  <section class="hero">
    <div class="hero-photo" role="img" aria-label="Photo of smiling university students holding books on campus"></div>
    <svg class="hero-shade" width="848" height="421" viewBox="0 0 848 421" aria-hidden="true">
      <polygon points="0,0 300,0 405,421 0,421" fill="rgba(40,42,44,0.62)"/>
    </svg>
    <div class="brand"><span class="brand-dot"></span>Vellumcheck</div>
    <div class="hero-rule"></div>
    <h1 class="headline">Professional,<br>English language<br>proofreading.</h1>
  </section>

  <section class="benefits">
    <div class="benefit b1"><span class="benefit-num">1</span><p class="benefit-text">Help with English as a second language (ESL).</p></div>
    <div class="benefit b2"><span class="benefit-num">2</span><p class="benefit-text">Proofreading by a native English speaker with an Honours degree in English.</p></div>
    <div class="benefit b3"><span class="benefit-num">3</span><p class="benefit-text">Includes correcting all English language errors, spelling and grammar mistakes, reference checking and editing for style, coherence and clarity.</p></div>
  </section>

  <h2 class="tag tag-docs">Documents include:</h2>
  <ul class="doc-list">
    <li>Essays and assignments</li>
    <li>Theses</li>
    <li>Resumes</li>
    <li>Business correspondence</li>
    <li>Training manuals</li>
    <li>Newsletters</li>
    <li>Advertising copy</li>
    <li>Brochures, catalogues and media releases</li>
    <li>Websites</li>
    <li>Presentations and speeches</li>
    <li>Novels and short stories</li>
  </ul>

  <h2 class="tag tag-price">Price guide:</h2>
  <ul class="price-list">
    <li><svg width="12" height="12" viewBox="0 0 12 12"><rect width="12" height="12" fill="var(--teal)"/><path d="M2.5 6.2 L5 8.6 L9.5 3.4" stroke="#fff" stroke-width="1.8" fill="none"/></svg>Discounts for not-for-profit organisations.</li>
    <li><svg width="12" height="12" viewBox="0 0 12 12"><rect width="12" height="12" fill="var(--teal)"/><path d="M2.5 6.2 L5 8.6 L9.5 3.4" stroke="#fff" stroke-width="1.8" fill="none"/></svg>Great student discount rate: <strong>$25 per hour</strong><br>(roughly 1000 words - 4 pages - of well-written text).</li>
    <li><svg width="12" height="12" viewBox="0 0 12 12"><rect width="12" height="12" fill="var(--teal)"/><path d="M2.5 6.2 L5 8.6 L9.5 3.4" stroke="#fff" stroke-width="1.8" fill="none"/></svg>Package deals on documents over 50,000 words.</li>
    <li><svg width="12" height="12" viewBox="0 0 12 12"><rect width="12" height="12" fill="var(--teal)"/><path d="M2.5 6.2 L5 8.6 L9.5 3.4" stroke="#fff" stroke-width="1.8" fill="none"/></svg>Fast, negotiable time frames.</li>
    <li class="note">(Same day service available by special arrangement.)</li>
  </ul>

  <div class="hand-phone" role="img" aria-label="Photo of a hand holding a smartphone showing a client testimonial"></div>
  <blockquote class="quote-card">
    <span class="mark">“</span>Harriet understood our requirements quickly and has been fantastic at delivering quality work, on time and within an agreed budget. It's a pleasure to work with her.<span class="mark">”</span>
    <p class="who">- Clara Whitby<br>Operations Manager<br>northgateAU</p>
    <p class="mini-brand">Vellumcheck</p>
  </blockquote>

  <footer class="footer">
    <p class="footer-call">Contact Harriet for an obligation free quote:</p>
  </footer>
  <address class="contact" style="font-style:normal">
    <div class="contact-row"><svg width="14" height="14" viewBox="0 0 24 24"><path fill="#fff" d="M6.6 10.8a15 15 0 0 0 6.6 6.6l2.2-2.2c.3-.3.7-.4 1-.2 1.1.4 2.3.6 3.6.6.6 0 1 .4 1 1V20c0 .6-.4 1-1 1A17 17 0 0 1 3 4c0-.6.4-1 1-1h3.5c.6 0 1 .4 1 1 0 1.3.2 2.5.6 3.6.1.3 0 .7-.2 1z"/></svg>0491 570 156</div>
    <div class="contact-row small"><svg width="14" height="11" viewBox="0 0 14 11"><rect width="14" height="11" fill="#fff"/><path d="M0 0 L7 6 L14 0" stroke="var(--teal)" stroke-width="1.3" fill="none"/></svg>proofing@vellumcheck.com.au</div>
    <div class="contact-row"><svg width="14" height="14" viewBox="0 0 14 14"><g fill="none" stroke="#fff" stroke-width="1.2"><circle cx="7" cy="7" r="6"/><ellipse cx="7" cy="7" rx="2.6" ry="6"/><path d="M1 7h12M2 4h10M2 10h10"/></g></svg>vellumcheck.com.au</div>
  </address>

</main>
</body>
</html>
```